Innovative approaches to treat addiction

PowerPoint on different techniques
Add graphics to screen
Easy to follow
I've provided the PowerPoint w content
Now make it pretty
And
hand outs for them to follow and take notes
Can you also add my bio:
Mara J. Thornquist, MS LCADC is a licensed Psychotherapist with a specialty in Addiction Disorders and over 22 years of clinical experience. Her integrative approach to counseling combines years of clinical experience with cognitive behavioral and traditional psychotherapy, with holistic therapies including; mindfulness, NLP, hypnotherapy, yoga therapy, reiki, motivational and wellness coaching.
Handout materials for them to follow and take notes

```html
<!DOCTYPE html>
<html lang="en">
<head>
<meta charset="utf-8">
<title>Innovative Techniques to Treat Disorders</title>
<link href="https://fonts.googleapis.com/css2?family=Arimo:ital,wght@0,400;0,700;1,400&display=swap" rel="stylesheet">
<style>
  :root {
    --header-dark: #0b3470;
    --header-mid: #1a5aa8;
    --header-light: #3f86c9;
    --body-bg: #ffffff;
    --body-edge: #e6e8ea;
    --bubble-top: #f4fbfd;
    --bubble-bottom: #cfe8ef;
    --bubble-text: #1e3a66;
    --connector: #3a3a3a;
    --accent-blue: #1f4f9e;
    --note-text: #111111;
    --footer-text: #9bb4d6;
    --figure-dark: #1c1c1c;
    --figure-soft: #4a3f5c;
    --white: #ffffff;
  }
  * { box-sizing: border-box; margin: 0; padding: 0; }
  html, body { width: 1200px; height: 900px; overflow: hidden; }
  body { font-family: "Arimo", Arial, sans-serif; background: var(--body-bg); }

  .slide {
    position: relative;
    width: 1200px;
    height: 900px;
    overflow: hidden;
    background: radial-gradient(ellipse at 50% 50%, var(--body-bg) 60%, var(--body-edge) 100%);
  }

  .slide-header {
    position: absolute;
    left: 0; top: 0;
    width: 1200px; height: 206px;
    background: linear-gradient(100deg, var(--header-dark) 0%, var(--header-mid) 45%, var(--header-light) 80%, var(--header-mid) 100%);
  }
  .slide-header::after {
    content: "";
    position: absolute;
    left: 0; bottom: 0;
    width: 100%; height: 10px;
    background: linear-gradient(90deg, rgba(255,255,255,0.15), rgba(255,255,255,0.35), rgba(255,255,255,0.1));
  }

  .header-emblem {
    position: absolute;
    left: 50px; top: 0;
    width: 175px; height: 206px;
    background: linear-gradient(180deg, rgba(255,255,255,0.18), rgba(255,255,255,0.04));
  }

  .slide-title {
    position: absolute;
    left: 244px; top: 44px;
    color: var(--white);
    font-weight: 400;
    font-size: 32px;
    line-height: 50px;
  }
  .slide-title .subtitle { display: block; padding-left: 12px; }

  .diagram { position: absolute; left: 0; top: 0; width: 1200px; height: 900px; }
  .bubble-label {
    font-family: "Arimo", Arial, sans-serif;
    font-size: 27px;
    fill: var(--bubble-text);
    text-anchor: middle;
  }

  .center-figure {
    position: absolute;
    left: 508px; top: 362px;
    width: 154px; height: 168px;
    background: linear-gradient(180deg, var(--figure-soft), var(--figure-dark));
  }

  .tagline {
    position: absolute;
    left: 0; top: 728px;
    width: 1200px;
    text-align: center;
    color: var(--accent-blue);
    font-size: 42px;
    font-weight: 400;
  }

  .disclaimer {
    position: absolute;
    left: 97px; top: 800px;
    width: 1005px;
    font-size: 17px;
    font-style: italic;
    color: var(--note-text);
    line-height: 22px;
  }

  .slide-footer {
    position: absolute;
    left: 0; top: 860px;
    width: 1200px; height: 40px;
    background: linear-gradient(90deg, var(--header-dark), var(--header-mid) 50%, var(--header-dark));
    color: var(--footer-text);
    font-size: 16px;
  }
  .slide-footer span { position: absolute; top: 13px; }
  .footer-date { left: 28px; }
  .footer-title { left: 0; width: 1200px; text-align: center; }
  .footer-author { right: 22px; }
</style>
</head>
<body>
<main class="slide">
  <header class="slide-header">
    <div class="header-emblem" role="img" aria-label="Outline of a head in profile with gears inside"></div>
    <h1 class="slide-title">Innovative Techniques to Treat Disorders<span class="subtitle">Results of the tools you will learn</span></h1>
  </header>

  <svg class="diagram" viewBox="0 0 1200 900">
    <defs>
      <linearGradient id="bubbleFill" x1="0" y1="0" x2="0" y2="1">
        <stop offset="0" stop-color="var(--bubble-top)"/>
        <stop offset="1" stop-color="var(--bubble-bottom)"/>
      </linearGradient>
      <filter id="bubbleShadow" x="-20%" y="-20%" width="140%" height="150%">
        <feDropShadow dx="2" dy="4" stdDeviation="3" flood-color="#000" flood-opacity="0.3"/>
      </filter>
    </defs>

    <g class="connectors" stroke="var(--connector)" stroke-width="1.3">
      <line x1="586" y1="445" x2="601" y2="334"/>
      <line x1="560" y1="420" x2="430" y2="364"/>
      <line x1="640" y1="420" x2="776" y2="364"/>
      <line x1="560" y1="480" x2="430" y2="556"/>
      <line x1="640" y1="480" x2="776" y2="556"/>
      <line x1="601" y1="500" x2="601" y2="592"/>
    </g>

    <g class="bubbles" fill="url(#bubbleFill)" filter="url(#bubbleShadow)">
      <ellipse cx="601" cy="279" rx="131" ry="55"/>
      <ellipse cx="329" cy="338" rx="131" ry="55"/>
      <ellipse cx="875" cy="338" rx="131" ry="55"/>
      <ellipse cx="329" cy="581" rx="131" ry="55"/>
      <ellipse cx="875" cy="581" rx="131" ry="55"/>
      <ellipse cx="601" cy="646" rx="131" ry="55"/>
    </g>

    <g class="labels">
      <text class="bubble-label" x="601" y="270">Patient</text>
      <text class="bubble-label" x="601" y="306">Rapport</text>
      <text class="bubble-label" x="329" y="329">Patient</text>
      <text class="bubble-label" x="329" y="365">Retention</text>
      <text class="bubble-label" x="875" y="329">Healing</text>
      <text class="bubble-label" x="875" y="365">Time</text>
      <text class="bubble-label" x="329" y="572">Stress and</text>
      <text class="bubble-label" x="329" y="608">Burnout</text>
      <text class="bubble-label" x="875" y="572">Treatment</text>
      <text class="bubble-label" x="875" y="608">Compliance</text>
      <text class="bubble-label" x="601" y="637">Fun &amp;</text>
      <text class="bubble-label" x="601" y="673">Sustainable</text>
    </g>
  </svg>

  <div class="center-figure" role="img" aria-label="Illustration of a head silhouette with a colourful brain"></div>

  <p class="tagline">Anyone can do it!</p>

  <p class="disclaimer">Note: These techniques are not a replacement for standard medical procedures, but work in conjunction with them by freeing the patient of feelings or attitudes that may be compromising his/her natural immune system.</p>

  <footer class="slide-footer">
    <span class="footer-date">8/26/2016</span>
    <span class="footer-title">Innovative &nbsp;Techniques to Treat Disorders</span>
    <span class="footer-author">Mara J. Thornquist</span>
  </footer>
</main>
</body>
</html>
```